100% West Australian Static Banner

I require a static banner to go on a couple of pages in our website (under development) that highlights that we are a 100% Western Australian Owned & Operated company. I would prefer the banner to be in our company colours (blue shades & grey). I also would like it to be eye catching and modern in design. I have included a 100% West Australian rubber stamp logo to be used as well as including our logo so you know our colours. The banner needs to be 1139 x 350 pixels in size.

Target Market(s)

B2B

Requirements
Must have
• Our rubber stamp 100% West Australian logo
• Modern Eye Catching design
• Blue shaded background
Nice to have
• Shading background similar our logo blue colours
• 100% logo can be reversed out if required or colour changed
• Larger text saying - 100% West Australian Owned & Operated

```html
<!DOCTYPE html>
<html lang="en">
<head>
<meta charset="utf-8">
<title>100% West Australian Owned &amp; Operated</title>
<link rel="stylesheet" href="https://fonts.googleapis.com/css2?family=Open+Sans:wght@400&display=swap">
<style>
  :root {
    --page: #ffffff;
    --blue-mid: #1670bb;
    --blue-deep: #1656a4;
    --blue-navy: #1b4d95;
    --blue-light: #2a9ad6;
    --blue-sky: #3aa6df;
    --glow: #ffffff;
    --text: #ffffff;
    --brand: #1a5aa8;
  }
  html, body {
    margin: 0;
    padding: 0;
    width: 1200px;
    height: 367px;
    overflow: hidden;
    background: var(--page);
  }
  .canvas {
    position: relative;
    width: 1200px;
    height: 367px;
    background: var(--page);
  }
  .banner {
    position: absolute;
    left: 15px;
    top: 2px;
    width: 1142px;
    height: 350px;
    overflow: hidden;
  }
  .banner-art {
    position: absolute;
    inset: 0;
    display: block;
  }
  .brand {
    position: absolute;
    left: 200px;
    top: 165px;
    transform: translate(-50%, -50%);
    margin: 0;
    white-space: nowrap;
    font-family: "Open Sans", sans-serif;
    font-weight: 400;
    font-size: 26px;
    color: var(--brand);
  }
  .headline {
    position: absolute;
    left: 323px;
    top: 94px;
    width: 650px;
    margin: 0;
    text-align: center;
    font-family: "Open Sans", sans-serif;
    font-weight: 400;
    font-size: 53px;
    line-height: 72px;
    color: var(--text);
    letter-spacing: -0.5px;
  }
</style>
</head>
<body>
<div class="canvas">
  <section class="banner">
    <svg class="banner-art" viewBox="0 0 1142 350" width="1142" height="350" aria-hidden="true">
      <defs>
        <linearGradient id="sky" x1="0" y1="0" x2="1" y2="0">
          <stop offset="0" stop-color="var(--blue-mid)"/>
          <stop offset="0.55" stop-color="#1a77c2"/>
          <stop offset="1" stop-color="var(--blue-light)"/>
        </linearGradient>
        <linearGradient id="ribbon" x1="0" y1="0" x2="1" y2="0">
          <stop offset="0" stop-color="#1e86cc"/>
          <stop offset="1" stop-color="var(--blue-sky)"/>
        </linearGradient>
        <linearGradient id="lower" x1="0" y1="0" x2="1" y2="0">
          <stop offset="0" stop-color="var(--blue-navy)"/>
          <stop offset="0.5" stop-color="#1c64ae"/>
          <stop offset="1" stop-color="var(--blue-light)"/>
        </linearGradient>
        <radialGradient id="halo" cx="0.5" cy="0.5" r="0.5">
          <stop offset="0" stop-color="var(--glow)" stop-opacity="1"/>
          <stop offset="0.45" stop-color="var(--glow)" stop-opacity="0.85"/>
          <stop offset="1" stop-color="var(--glow)" stop-opacity="0"/>
        </radialGradient>
      </defs>
      <rect width="1142" height="350" fill="url(#sky)"/>
      <path d="M630 0 C710 40 790 95 890 110 C990 125 1080 100 1142 80 L1142 0 Z" fill="url(#ribbon)"/>
      <path d="M0 215 C140 265 300 275 450 235 C620 190 820 130 1000 115 C1070 108 1110 105 1142 100 L1142 205 C1040 225 900 230 760 245 C600 265 420 290 250 350 L0 350 Z" fill="var(--blue-deep)"/>
      <path d="M0 235 C150 285 300 290 460 255 C640 215 860 220 1142 205 L1142 350 L0 350 Z" fill="url(#lower)" role="img" aria-label="Soft dotted texture across the lower wave"/>
      <circle cx="200" cy="165" r="145" fill="url(#halo)"/>
    </svg>
    <p class="brand">Harbourline</p>
    <h1 class="headline">100% West Australian<br>Owned &amp; Operated</h1>
  </section>
</div>
</body>
</html>
```